Cat-products company needs smart, yet endearing, business card

We need a business card design for a new, but up-and-running, business based in Honolulu, Hawaii. The business is Purrlane Nest Co. Our first product is the most environmentally-friendly cat grass kit ever seen on the planet. Future products, currently in the R&D phase, will include a variety of exciting cat scratchers. We also do consulting work to help apartment-dwellers make their home more cat-friendly and, in the future, plan on doing full, custom installs of structure to create high walkways for cats.

Target Market(s)

Middle-aged, apartment-dwelling, middle-class workers who own 1 or more cats and who dote on them.

Industry/Entity Type

Pet Care

Contact Information for Business Card

A striking, professional, yet warm and friendly design is what we're after.

Font styles to use
Serif
Sans Serif
Other font styles liked:
• Comfortaa

Colors

Designer to choose colors to be used in the design.

Requirements
Must have
• The company logo: (see attachment)
• The company name: Purrlane Nest Co
• The web address: www.purrlanenestco.example
• Email: support@purrlanenestco.example
• Phone: +1 (808) 555 0172
• Update (Fri Jun 30 3017 7:45pm Hawaii Time) I would like, is possible, uploaded picture of the cat grass kit on the back of the card with some text along the lines of: Purrlane Nest Co - Where The Freshest Kitty Sprouts Begin
Nice to have
• A cat picture, cartoon, real or silhouette that illustrates cats in action and/or relaxing; ie using the apartment space to live, play and relax in and being well-contented.
• Most of the website is done in the font: Comfortaa. It might be nice to continue using this for brand consistency.
Should not have
• Hard-to-read fonts.

```html
<!DOCTYPE html>
<html lang="en">
<head>
<meta charset="utf-8">
<title>Purrlane Nest Co – Business Card</title>
<link rel="stylesheet" href="https://fonts.googleapis.com/css2?family=Comfortaa:wght@400;700&display=swap">
<style>
  :root {
    --backdrop: #8a7210;
    --card: #ffffff;
    --brown: #5a3530;
    --gold: #f7ad1a;
    --rule: #a8862a;
    --muted: #8b6a2a;
    --icon: #7a1f1f;
    --cat-fill: #9a7448;
  }
  * { margin: 0; padding: 0; box-sizing: border-box; }
  html, body { width: 1200px; height: 1200px; overflow: hidden; }
  body {
    background: var(--backdrop);
    font-family: "Comfortaa", sans-serif;
    position: relative;
  }
  .card {
    position: absolute;
    width: 840px;
    height: 480px;
    background: var(--card);
  }
  .card--front { left: 54px; top: 105px; }
  .card--back { left: 273px; top: 644px; }

  .brand {
    position: absolute;
    display: flex;
    flex-direction: column;
    align-items: center;
    gap: 22px;
    transform: translateX(-50%);
  }
  .card--front .brand { left: 210px; top: 150px; }
  .card--back .brand { left: 422px; top: 130px; }
  .brand__mark {
    width: 96px; height: 96px;
    border-radius: 50%;
    background: var(--brown);
  }
  .brand__name {
    font-weight: 700;
    font-size: 34px;
    color: var(--gold);
    white-space: nowrap;
    letter-spacing: 0.5px;
  }

  .divider {
    position: absolute;
    left: 419px; top: 94px;
    width: 2px; height: 263px;
    background: var(--rule);
  }

  .person { position: absolute; left: 478px; top: 88px; }
  .person__name { font-size: 20px; font-weight: 700; color: var(--brown); }
  .person__name .accent { color: var(--gold); }
  .person__role { font-size: 13px; color: var(--muted); margin-top: 8px; }

  .contacts { position: absolute; left: 478px; top: 193px; list-style: none; }
  .contacts li {
    display: flex; align-items: center;
    height: 20px; margin-bottom: 34px;
    font-size: 13px; color: var(--brown);
  }
  .contacts li:nth-child(2) { margin-bottom: 32px; }
  .contacts svg { width: 16px; height: 16px; margin-right: 44px; flex: none; }

  .card__footer {
    position: absolute;
    right: 130px;
    font-size: 13px;
  }
  .card--front .card__footer { top: 436px; color: var(--muted); }
  .card--back .card__footer { top: 441px; color: var(--brown); right: 125px; }

  .cat-art {
    position: absolute;
    width: 72px; height: 63px;
    border-radius: 10px;
    background: linear-gradient(135deg, #b08a5a, var(--cat-fill) 60%, #6b4c32);
  }
  .card--front .cat-art { left: 725px; top: 388px; }
  .card--back .cat-art { left: 727px; top: 390px; }
</style>
</head>
<body>
  <section class="card card--front">
    <div class="brand">
      <div class="brand__mark"></div>
      <div class="brand__name">Purrlane Nest Co</div>
    </div>

    <div class="divider"></div>

    <div class="person">
      <div class="person__name">Marcus <span class="accent">Kealoha</span></div>
      <div class="person__role">CEO</div>
    </div>

    <ul class="contacts">
      <li>
        <svg viewBox="0 0 16 16" aria-hidden="true"><path fill="var(--icon)" d="M3.2 1.2l2.4 2.6-1.3 1.8c.9 2 2.3 3.5 4.3 4.5l1.8-1.3 2.6 2.4-1.4 2.3C6.4 13.3 2.6 9.5 1 4.3z"/></svg>
        +1 (808) 555 0172
      </li>
      <li>
        <svg viewBox="0 0 16 16" aria-hidden="true"><rect x="1" y="3" width="14" height="10" fill="var(--icon)"/><path d="M1.5 3.5L8 9l6.5-5.5M1.5 12.5l5-4.5M14.5 12.5l-5-4.5" stroke="#fff" stroke-width="1" fill="none"/></svg>
        support@purrlanenestco.example
      </li>
      <li>
        <svg viewBox="0 0 16 16" aria-hidden="true" fill="none" stroke="var(--icon)" stroke-width="1"><circle cx="8" cy="8" r="6.5"/><ellipse cx="8" cy="8" rx="3" ry="6.5"/><path d="M1.5 8h13M2.5 4.8h11M2.5 11.2h11"/></svg>
        www.purrlanenestco.example
      </li>
    </ul>

    <div class="card__footer">Purrlane Nest Co</div>
    <div class="cat-art" role="img" aria-label="Small flat illustration of a seated tabby cat"></div>
  </section>

  <section class="card card--back">
    <div class="brand">
      <div class="brand__mark"></div>
      <div class="brand__name">Purrlane Nest Co</div>
    </div>

    <div class="card__footer">www.purrlanenestco.example</div>
    <div class="cat-art" role="img" aria-label="Small flat illustration of a seated tabby cat"></div>
  </section>
</body>
</html>
```